Business Name is TB Glamworks - Make-up Artist

I'm looking for an attractive and eye catching business card for for mobile make-up artist business. On the front of the card, I just want the name TB Glamworks in feminine type cursive writing and underneath my name Tessa Bourne and Make-Up Artist.
On the back of the card, I would like written down one side the following;
Make-Up Tutorials
Bridal
Photography
Debutante
Formals
Family Portraits
I would also like the following details as well as the Chatterbook and Pictoflow Icons;
Mobile: 0482 615 379
Email: tessabourne@maildrop-example.com
Website: tessabourne.velqora-example.com
Certificate III in Make-Up
Also, I would like a section that says Your Next Appointment and a space to put that information.
I would also like the Velqora Symbol on the bottom right hand corner (I have attached)

Target Market(s)

Mostly females

Industry/Entity Type

Makeup

Contact Information for Business Card

TB Glamworks
Tessa Bourne - Make-Up Artist

Font styles to use
Script

Colors
b768aa
886aae
e34297

Requirements
Must have
• Mobile: 0482 615 379
• Email: tessabourne@maildrop-example.com
• Website: tessabourne.velqora-example.com
• Certificate III in Make-Up
Nice to have
• Something to do with make-up like a smudged lipstick or some eye shadow
Should not have
• Don't want it too busy

```html
<!DOCTYPE html>
<html lang="en">
<head>
<meta charset="utf-8">
<title>TB Glamworks – Business Card</title>
<link rel="stylesheet" href="https://fonts.googleapis.com/css2?family=Montserrat:wght@400;500;600;700&display=swap">
<style>
  :root {
    --magenta: #e3168d;
    --pink: #e34297;
    --orchid: #b768aa;
    --violet: #886aae;
    --purple: #8a55b8;
    --ink: #2a2a2a;
    --paper: #ffffff;
    --backdrop: #ecebef;
    --rule: #3a3a3a;
    --partner: #1f7a33;
  }
  * { box-sizing: border-box; margin: 0; padding: 0; }
  html, body {
    width: 1200px; height: 800px; overflow: hidden;
    background: var(--backdrop);
    font-family: "Montserrat", sans-serif;
  }
  .canvas { position: relative; width: 1200px; height: 800px; }

  .card {
    position: absolute; top: 245px;
    width: 540px; height: 309px;
    background: var(--paper);
    border-radius: 4px;
    box-shadow: 0 2px 10px rgba(0,0,0,.12);
    overflow: hidden;
  }

  /* ---------- back ---------- */
  .card--back { left: 40px; }
  .back__band {
    position: absolute; left: 0; top: 0; width: 100%; height: 190px;
    background: linear-gradient(20deg, var(--magenta) 0%, var(--orchid) 55%, var(--purple) 100%);
  }
  .contact {
    position: absolute; left: 20px; top: 98px; width: 215px;
    color: var(--paper); text-align: center;
    font-size: 11.5px; line-height: 1.45; font-weight: 400;
  }
  .contact__cert { font-weight: 700; }
  .social {
    position: absolute; left: 200px; top: 36px; width: 150px;
    display: flex; justify-content: center; gap: 12px;
  }
  .social__item {
    display: flex; align-items: center; gap: 4px;
    color: var(--paper); font-size: 9.5px; font-weight: 500;
  }
  .social__dot {
    width: 12px; height: 12px; border-radius: 50%;
    border: 1.5px solid var(--paper);
  }
  .divider {
    position: absolute; left: 274px; top: 66px;
    width: 1.5px; height: 100px; background: var(--paper);
  }
  .services {
    position: absolute; left: 300px; top: 62px; width: 220px;
    color: var(--paper); text-align: center;
    font-size: 12.5px; line-height: 1.5; font-weight: 400;
  }
  .services__sep { margin: 0 6px; }
  .appointment {
    position: absolute; left: 195px; top: 178px;
    width: 235px; height: 24px;
    border: 1.5px solid var(--violet); border-radius: 12px;
    background: var(--paper); color: var(--ink);
    font-size: 10.5px; font-weight: 500; letter-spacing: .04em;
    display: flex; align-items: center; justify-content: center;
  }
  .write-line { position: absolute; height: 1px; background: var(--rule); }
  .write-line--tail { left: 430px; top: 190px; width: 30px; }
  .write-line--one  { left: 120px; top: 240px; width: 350px; }
  .write-line--two  { left: 120px; top: 272px; width: 350px; }
  .partner {
    position: absolute; right: 14px; top: 196px;
    display: flex; align-items: center; gap: 4px;
    color: var(--partner); font-size: 10px; font-weight: 600;
  }
  .partner__dot { width: 12px; height: 12px; border-radius: 50%; background: var(--partner); }

  /* ---------- front ---------- */
  .card--front { left: 620px; }
  .brand {
    position: absolute; left: 0; top: 46px; width: 100%;
    display: flex; flex-direction: column; align-items: center; gap: 12px;
  }
  .brand__circle {
    width: 104px; height: 104px; border-radius: 50%;
    background: linear-gradient(180deg, var(--violet) 0%, var(--pink) 100%);
  }
  .brand__name {
    color: var(--magenta); font-size: 24px; font-weight: 600;
  }
  .owner {
    position: absolute; left: 0; top: 232px; width: 100%;
    text-align: center; color: var(--ink); font-size: 16px;
  }
  .owner__name { font-weight: 700; margin-right: 8px; }
  .owner__role { font-weight: 400; }
</style>
</head>
<body>
<main class="canvas">

  <section class="card card--back" aria-label="Business card back">
    <div class="back__band"></div>

    <div class="social">
      <span class="social__item"><span class="social__dot"></span>Pictoflow</span>
      <span class="social__item"><span class="social__dot"></span>Chatterbook</span>
    </div>
    <div class="divider"></div>

    <div class="contact">
      <p>0482 615 379</p>
      <p>tessabourne@maildrop-example.com</p>
      <p>tessabourne.velqora-example.com</p>
      <p class="contact__cert">Certificate III in Make-Up</p>
    </div>

    <div class="services">
      <p>Make-Up Tutorials</p>
      <p>Bridal<span class="services__sep">|</span>Photography</p>
      <p>Debutante<span class="services__sep">|</span>Formals</p>
      <p>Family Portraits</p>
    </div>

    <div class="appointment">YOUR NEXT APPOINTMENT</div>
    <div class="write-line write-line--tail"></div>
    <div class="write-line write-line--one"></div>
    <div class="write-line write-line--two"></div>

    <div class="partner"><span class="partner__dot"></span>Velqora</div>
  </section>

  <section class="card card--front" aria-label="Business card front">
    <div class="brand">
      <div class="brand__circle"></div>
      <p class="brand__name">TB Glamworks</p>
    </div>
    <p class="owner"><span class="owner__name">Tessa Bourne</span><span class="owner__role">Make-Up Artist</span></p>
  </section>

</main>
</body>
</html>
```